Bright Volley Pickleball Tournament

Design a poster for the Copper Ridge Dink Series, a pickleball tournament series. Each event will have it's own poster with a different design. The posters should be different but related graphically. The first assignment is Posters 1 and 2. The posters should be bold, exciting, fun and show movement. The attached files are for content, hierarchy for text but not design. Logo typeface: Legend 54. Logo blue: cmyk blue: 2b3990 R: 43 G:57 B:144
Please contact me with questions.

```html
<!DOCTYPE html>
<html lang="en">
<head>
<meta charset="utf-8">
<title>Bright Volley Pickleball Tournament – Copper Ridge Dink Series</title>
<link href="https://fonts.googleapis.com/css2?family=Exo+2:ital,wght@1,800;1,900&family=Saira+Condensed:wght@700&family=Teko:wght@600&family=Arimo:wght@400;700&display=swap" rel="stylesheet">
<style>
  :root {
    --stage: #f2f2f2;
    --navy: #262c63;
    --navy-deep: #1d2250;
    --band: #3b3fae;
    --band-warm: #6a3f78;
    --ball: #e9d23c;
    --ball-shade: #d6b92a;
    --red: #e3101b;
    --red-dark: #a8060d;
    --yellow: #f4ea1d;
    --white: #ffffff;
    --silver-top: #ffffff;
    --silver-bottom: #b9bcc4;
    --date-ink: #26307a;
  }
  * { margin: 0; padding: 0; box-sizing: border-box; }
  html, body { width: 1200px; height: 1000px; overflow: hidden; }
  body { background: var(--stage); position: relative; font-family: "Arimo", Arial, sans-serif; }

  .poster {
    position: absolute; left: 228px; top: 15px; width: 740px; height: 958px;
    background: linear-gradient(160deg, var(--navy) 0%, var(--navy-deep) 55%, var(--navy) 100%);
    overflow: hidden; color: var(--white); text-align: center;
  }
  .motion-bands { position: absolute; inset: 0; width: 100%; height: 100%; }

  .series-mark { position: absolute; left: 0; right: 0; top: 40px; }
  .series-mark__dot {
    width: 56px; height: 56px; border-radius: 50%; background: var(--ball); margin: 0 auto 18px;
  }
  .series-mark__name {
    font-family: "Teko", "Oswald", sans-serif; font-weight: 600; font-size: 38px; line-height: 32px;
    color: var(--white); letter-spacing: 1px; text-transform: uppercase;
  }

  .hero-ball {
    position: absolute; left: 178px; top: 215px; width: 330px; height: 330px; border-radius: 50%;
    background: radial-gradient(circle at 40% 35%, var(--ball) 60%, var(--ball-shade) 100%);
    box-shadow: 0 0 0 14px rgba(70, 80, 200, .35);
  }

  .event-title {
    position: absolute; left: 0; right: 0; top: 258px;
    font-family: "Exo 2", sans-serif; font-style: italic; font-weight: 900;
    color: var(--red); text-transform: uppercase; line-height: .9;
    text-shadow: 2px 2px 0 var(--white), -2px -2px 0 var(--white), 2px -2px 0 var(--white), -2px 2px 0 var(--white), 6px 6px 0 var(--red-dark);
  }
  .event-title__top { display: block; font-size: 86px; }
  .event-title__main { display: block; font-size: 112px; margin-top: 6px; }

  .date-plate {
    position: absolute; left: 182px; top: 477px; width: 362px; height: 60px; border-radius: 10px;
    background: linear-gradient(var(--silver-top), var(--silver-bottom));
    transform: skewX(-6deg); box-shadow: 0 3px 6px rgba(0,0,0,.4);
    color: var(--date-ink); padding-top: 8px;
  }
  .date-plate__date { font-family: "Exo 2", sans-serif; font-style: italic; font-weight: 800; font-size: 27px; line-height: 28px; }
  .date-plate__note { font-size: 10.5px; font-weight: 700; font-style: italic; }

  .kicker { font-family: "Saira Condensed", "Oswald", sans-serif; font-weight: 700; color: var(--yellow); text-transform: uppercase; }
  .sanction { position: absolute; left: 0; right: 0; top: 558px; font-size: 26px; }

  .rule { position: absolute; left: 277px; width: 183px; height: 2px; background: var(--white); }
  .rule--top { top: 609px; }
  .rule--bottom { top: 764px; }

  .details { position: absolute; left: 0; right: 0; top: 631px; font-weight: 700; font-size: 17px; line-height: 22px; }
  .details p + p { margin-top: 14px; }

  .sponsor { position: absolute; left: 0; right: 0; top: 793px; font-size: 22px; }
  .contact { position: absolute; left: 0; right: 0; top: 829px; font-size: 16px; line-height: 20px; }
  .venue { position: absolute; left: 0; right: 0; top: 886px; font-size: 15px; line-height: 20px; font-weight: 700; }
</style>
</head>
<body>
  <main class="poster">
    <svg class="motion-bands" viewBox="0 0 740 958" preserveAspectRatio="none" aria-hidden="true">
      <polygon points="40,0 140,0 360,520 260,520" fill="var(--band)" opacity=".35"/>
      <polygon points="560,0 620,0 740,290 740,430" fill="var(--band)" opacity=".55"/>
      <polygon points="0,80 30,80 120,300 0,230" fill="var(--band)" opacity=".5"/>
      <polygon points="620,440 740,400 740,560 600,620" fill="var(--band-warm)" opacity=".35"/>
      <polygon points="0,500 70,520 330,958 200,958 0,640" fill="var(--band-warm)" opacity=".45"/>
      <polygon points="0,800 40,770 120,958 60,958" fill="var(--band)" opacity=".5"/>
    </svg>

    <header class="series-mark">
      <div class="series-mark__dot"></div>
      <div class="series-mark__name">Copper Ridge<br>Dink Series</div>
    </header>

    <div class="hero-ball" role="img" aria-label="Large yellow pickleball behind the event title"></div>

    <h1 class="event-title">
      <span class="event-title__top">Bright</span>
      <span class="event-title__main">Volley</span>
    </h1>

    <div class="date-plate">
      <div class="date-plate__date">NOVEMBER 23-24, 2019</div>
      <div class="date-plate__note">THE WEEKEND BEFORE THANKSGIVING</div>
    </div>

    <h2 class="kicker sanction">NPA Sanctioned Pickleball Tournament</h2>
    <div class="rule rule--top"></div>

    <section class="details">
      <p>Women’s, Men’s and Mixed Doubles<br>3.0, 3.5, 4.0, 4.5, 5.0 Brackets</p>
      <p>Zephyr Glide Yellow Indoor Ball</p>
      <p>PRIZES!</p>
    </section>

    <div class="rule rule--bottom"></div>

    <h3 class="kicker sponsor">Sponsorship Opportunities Available</h3>
    <p class="contact">Questions: copperridgedinkseries@example.com<br>Registration: http://courtbrackets.example.com/</p>
    <p class="venue">Lakeview Sportsplex, 212 Birch Ave, Millbrook, MA<br>Venue of the 2019 NPA Atlantic Regional</p>
  </main>
</body>
</html>
```